Consulting company needs Business Cards - rough concept provided

I'm looking for someone to take our business card idea and make is slick and polished - to communicate our high-end, sophisticated, serious consulting business. We have a rough layout we did in-house. We are open to ideas on repo-ing elements, adjusting sizes, typefaces etc... within the general concept we've already come up with. We want it to be super-clean and sophisticated. We want to keep the white backgrounds, and blue brand colors. Our goal is to print with painted blue edges on thick cardstock. Thank you!!

```html
<!DOCTYPE html>
<html lang="en">
<head>
<meta charset="utf-8">
<title>Tall Heron – Business Cards</title>
<link rel="stylesheet" href="https://fonts.googleapis.com/css2?family=Mulish:wght@500;600;700;800&display=swap">
<style>
  :root {
    --page: #ececec;
    --card: #c9c9c9;
    --brand-blue: #4a98d6;
    --ink-white: #ffffff;
    --glow: rgba(214, 240, 255, 0.95);
    --glow-soft: rgba(190, 228, 250, 0.55);
    --line: rgba(225, 244, 255, 0.7);
  }
  * { box-sizing: border-box; margin: 0; padding: 0; }
  html, body { width: 1200px; height: 1200px; overflow: hidden; }
  body {
    background: var(--page);
    font-family: "Mulish", "Helvetica Neue", Arial, sans-serif;
    display: flex;
    flex-direction: column;
    align-items: center;
    justify-content: center;
    gap: 60px;
  }
  .card {
    position: relative;
    width: 880px;
    height: 503px;
    background-color: var(--card);
    overflow: hidden;
    box-shadow: 0 2px 6px rgba(0,0,0,0.08);
  }
  .card-light {
    position: absolute;
    inset: 0;
    width: 100%;
    height: 100%;
  }
  .card-back .statement {
    position: absolute;
    inset: 0;
    display: flex;
    align-items: center;
    justify-content: center;
    text-align: center;
    font-weight: 600;
    font-size: 33px;
    line-height: 67px;
    letter-spacing: 0.13em;
    text-transform: uppercase;
    color: var(--ink-white);
  }
  .statement .accent { color: var(--brand-blue); }

  .wordmark {
    position: absolute;
    top: 22px;
    left: 26px;
    right: 18px;
    font-weight: 600;
    font-size: 88px;
    line-height: 1;
    letter-spacing: 0.12em;
    color: var(--brand-blue);
    white-space: nowrap;
  }
  .person {
    position: absolute;
    left: 88px;
    top: 292px;
    text-transform: uppercase;
  }
  .person-name {
    font-weight: 800;
    font-size: 40px;
    letter-spacing: 0.03em;
    color: var(--brand-blue);
  }
  .person-role {
    font-weight: 700;
    font-size: 25px;
    letter-spacing: 0.05em;
    color: var(--ink-white);
    margin-top: 2px;
  }
  .contact {
    position: absolute;
    bottom: 30px;
    font-weight: 700;
    font-size: 15px;
    line-height: 18px;
    letter-spacing: 0.05em;
    color: var(--ink-white);
  }
  .contact-direct { left: 88px; }
  .contact-address { right: 40px; text-align: right; text-transform: uppercase; }
</style>
</head>
<body>

  <section class="card card-back" aria-label="Card back with mission statement">
    <svg class="card-light" viewBox="0 0 880 503" preserveAspectRatio="none" aria-hidden="true">
      <defs>
        <radialGradient id="back-glow-top" cx="0.83" cy="0.13" r="0.5">
          <stop offset="0" stop-color="var(--glow)"/>
          <stop offset="0.35" stop-color="var(--glow-soft)"/>
          <stop offset="1" stop-color="rgba(201,201,201,0)"/>
        </radialGradient>
        <radialGradient id="back-glow-bottom" cx="0.12" cy="0.82" r="0.35">
          <stop offset="0" stop-color="var(--glow)"/>
          <stop offset="0.4" stop-color="var(--glow-soft)"/>
          <stop offset="1" stop-color="rgba(201,201,201,0)"/>
        </radialGradient>
      </defs>
      <rect width="880" height="503" fill="url(#back-glow-top)"/>
      <rect width="880" height="503" fill="url(#back-glow-bottom)"/>
      <line x1="120" y1="0" x2="120" y2="503" stroke="var(--line)" stroke-width="1.5"/>
      <line x1="0" y1="62" x2="880" y2="62" stroke="var(--line)" stroke-width="1"/>
      <line x1="0" y1="440" x2="400" y2="440" stroke="var(--line)" stroke-width="1"/>
      <path d="M380 503 Q560 380 880 420" fill="none" stroke="var(--line)" stroke-width="1.2"/>
    </svg>
    <p class="statement">
      <span>
        <span class="accent">We help you</span> and your team<br>
        <span class="accent">achieve</span> your ultimate <span class="accent">vision</span><br>
        by combining your <span class="accent">DNA</span>, with<br>
        our own <span class="accent">unique approach</span> to<br>
        problem <span class="accent">solving</span> and <span class="accent">strategy</span>
      </span>
    </p>
  </section>

  <section class="card card-front" aria-label="Card front with name and contact details">
    <svg class="card-light" viewBox="0 0 880 503" preserveAspectRatio="none" aria-hidden="true">
      <defs>
        <radialGradient id="front-glow" cx="0.1" cy="0.55" r="0.5">
          <stop offset="0" stop-color="var(--glow)"/>
          <stop offset="0.4" stop-color="var(--glow-soft)"/>
          <stop offset="1" stop-color="rgba(201,201,201,0)"/>
        </radialGradient>
        <radialGradient id="front-glow-top" cx="0.55" cy="0.1" r="0.4">
          <stop offset="0" stop-color="var(--glow-soft)"/>
          <stop offset="1" stop-color="rgba(201,201,201,0)"/>
        </radialGradient>
      </defs>
      <rect width="880" height="503" fill="url(#front-glow)"/>
      <rect width="880" height="503" fill="url(#front-glow-top)"/>
      <line x1="800" y1="0" x2="800" y2="503" stroke="var(--line)" stroke-width="1.5"/>
      <line x1="0" y1="190" x2="880" y2="190" stroke="var(--line)" stroke-width="1"/>
      <line x1="60" y1="0" x2="60" y2="503" stroke="var(--line)" stroke-width="1"/>
    </svg>
    <h1 class="wordmark">TALL HERON</h1>
    <div class="person">
      <p class="person-name">Dana Whitford</p>
      <p class="person-role">Brand Consultant</p>
    </div>
    <p class="contact contact-direct">(555) 014 2297<br>dana@tallheron.com<br>tallheron.com</p>
    <p class="contact contact-address">4820 Linden Ave, Ste 210<br>Maple Grove<br>CA 90000</p>
  </section>

</body>
</html>
```